Hollow Lantern Double Sided Flyer Design

We need a double sided flyer (1/3 of an A4 which is 99mm x 210mm) developed for our Newcastle(NSW) tour. This flyer will be placed in tourist information centres and hotels. We want it to direct people to our website or be able to make bookings over the phone.

About Us:-
We are a city walking tour company that runs tours day or night. We run both day and night and will incorporate real history / real Hollow lantern. Some of the stories will be quite serious i.e.- there are infamous murders from 100 years ago, baffling court cases, even a bit of poetry written by murderers, suicides, love triangles, you name it. We will be telling the historical stories that tourists will not hear from any other tour provider. A bit of darkness, a bit of mystery and a bit of history theme.

We do no go for scares and let the very real stories deliver the entertainment for our guests. Our customers enjoy our tours, but it isn't light fun and frivolity. Our stories are being carefully crafted and are packed with unexpected twists, turns; revelations whilst remaining all 100% true. We deliver deep, rich, engaging stories.

Here are a few samples of quotes from the characters in our stories that may give you an idea of the kind of history we will cover:-

"There were bits of spines, bits of skulls, [and] finger bones spilled out all over the streets - I ended up filling three boxes. Children were playing with them for weeks”

"I had a close shave last night and now I want a close haircut.”

“She's a beautiful child', isn't she? She's the cause of all the trouble.”

“I did it because she would not come home with me.”

"I have killed my wife. I’m glad she’s dead.”

"Stand aside or I'll put a bullet through both of you."

“You villain, I'll teach you to take away my character."

“You’re not dead yet, you bastard!”

Our website, booking form and contact details can be viewed at www.hollowlantern-tours.com.au

Target Market(s)

Tourists

Industry/Entity Type

Tour

Colors

Designer to choose colors to be used in the design.

Requirements
Must have
• Vertical orientation please.
• Please also include a reference to a discount offer of 25% using the promo code "DARK".
Nice to have
• FRONT FLYER INFORMATION
• - Hollow Lantern Logo
• - "I have killed my wife; I'm glad she's dead."
• - Harbourside Buried Past Walk
• - 25% Discount Offer Codeword DARK
• - web address at the base; www.hollowlantern-tours.com.au
• BACK FLYER INFORMATION
• - "She's a beautiful child', isn't she? She's the cause of all the trouble.
• - Hollow Lantern Logo at the base along with the web address www.hollowlantern-tours.com.au
• - Blurb:- Hollow lantern brings back Newcastle's hidden past, the forgotten past, the dark past that may not want to be remembered.
• Real stories from the streets around you. Discover the histories you won't hear anywhere else. The forgotten stories of yesteryear finally get a chance to be told. Through you they get to live again.
Should not have
• GENERAL
• Please do not include the phone number, email address or social media icons. We want to drive online bookings.

```html
<!DOCTYPE html>
<html lang="en">
<head>
<meta charset="utf-8">
<title>Hollow Lantern – Double Sided Flyer</title>
<link href="https://fonts.googleapis.com/css2?family=Creepster&family=Lato:wght@400;700;900&display=swap" rel="stylesheet">
<style>
  :root {
    --page-bg: #d8d3cc;
    --ink-black: #141414;
    --char: #1f2222;
    --blood: #e3191b;
    --blood-deep: #a8080c;
    --paper-white: #ffffff;
    --body-font: "Lato", Arial, sans-serif;
    --drip-font: "Creepster", cursive;
  }
  * { box-sizing: border-box; margin: 0; padding: 0; }
  html, body { width: 1200px; height: 1200px; overflow: hidden; }
  body { background: var(--page-bg); position: relative; font-family: var(--body-font); }

  .flyer {
    position: absolute; overflow: hidden;
    background: radial-gradient(ellipse at 50% 40%, #2a2d2d 0%, var(--char) 55%, var(--ink-black) 100%);
    box-shadow: 0 6px 18px rgba(0,0,0,.35);
  }
  .flyer--front { left: 122px; top: 134px; width: 462px; height: 955px; }
  .flyer--back  { left: 643px; top: 134px; width: 461px; height: 946px; }

  .street-photo {
    position: absolute; left: 0; top: 0; width: 100%; height: 720px;
    background: linear-gradient(160deg, #4a4f50 0%, #2c3131 45%, #1b1e1e 80%, rgba(20,20,20,0) 100%);
    opacity: .85;
  }
  .blood-splatter { position: absolute; border-radius: 46% 54% 50% 50% / 52% 44% 56% 48%; }
  .flyer--front .blood-splatter {
    left: 100px; top: 225px; width: 270px; height: 265px;
    background: radial-gradient(circle at 50% 48%, var(--blood) 0%, var(--blood) 55%, rgba(200,15,18,.55) 72%, rgba(160,10,12,0) 100%);
  }
  .flyer--back .blood-splatter {
    left: 95px; top: 60px; width: 270px; height: 240px;
    background: radial-gradient(circle at 50% 48%, var(--blood) 0%, var(--blood) 55%, rgba(200,15,18,.55) 72%, rgba(160,10,12,0) 100%);
  }

  .brand {
    position: absolute; left: 0; width: 100%;
    display: flex; justify-content: center; align-items: center; gap: 10px;
    color: var(--paper-white); font-weight: 700; letter-spacing: 1px;
  }
  .brand__mark { width: 14px; height: 14px; background: var(--blood); }
  .flyer--front .brand { top: 132px; font-size: 30px; }
  .flyer--back .brand { top: 766px; font-size: 24px; }

  .quote { position: absolute; left: 0; width: 100%; text-align: center; color: var(--paper-white); }
  .quote__line { display: block; font-weight: 700; line-height: 1; }
  .quote__drip { display: block; font-family: var(--drip-font); line-height: 1; letter-spacing: 1px; }

  .flyer--front .quote { top: 255px; }
  .flyer--front .quote__line { font-size: 29px; margin: 3px 0; }
  .flyer--front .quote__drip { font-size: 54px; margin: 2px 0; }

  .flyer--back .quote { top: 78px; }
  .flyer--back .quote__line { font-size: 19px; margin: 2px 0; }
  .flyer--back .quote__line--gap { margin-top: 8px; }
  .flyer--back .quote__drip { font-size: 46px; margin: 2px 0; }

  .offer { position: absolute; left: 0; top: 590px; width: 100%; text-align: center; }
  .offer__tour { color: var(--paper-white); font-weight: 700; font-size: 24px; }
  .offer__discount { color: var(--blood); font-weight: 700; font-size: 54px; line-height: 1.05; margin-top: 6px; }
  .offer__label { color: var(--paper-white); font-weight: 700; font-size: 36px; line-height: 1.1; }
  .offer__code { color: var(--blood); font-family: var(--drip-font); font-size: 92px; line-height: 1; margin-top: 8px; }

  .web { position: absolute; left: 0; width: 100%; text-align: center; font-weight: 700; }
  .flyer--front .web { top: 842px; color: var(--paper-white); font-size: 25px; }
  .flyer--back .web { top: 884px; color: var(--blood); font-size: 25px; }

  .torn-band { position: absolute; left: 0; width: 100%; }
  .flyer--front .torn-band { bottom: 0; height: 48px; }
  .flyer--back .torn-band { top: 410px; height: 264px; }

  .blurb { position: absolute; left: 36px; right: 36px; top: 462px; text-align: center; color: var(--paper-white); font-size: 16.5px; line-height: 1.22; }
  .blurb p + p { margin-top: 10px; }

  .booking-note { position: absolute; left: 0; top: 810px; width: 100%; text-align: center; color: var(--paper-white); font-weight: 700; font-size: 19px; line-height: 1.25; }
</style>
</head>
<body>

<section class="flyer flyer--front" aria-label="Flyer front">
  <div class="street-photo" role="img" aria-label="Dark photograph of an old brick street building at night"></div>
  <div class="brand"><span class="brand__mark"></span><span>HOLLOW LANTERN</span></div>
  <div class="blood-splatter" role="img" aria-label="Red blood splatter"></div>
  <div class="quote">
    <span class="quote__line">I HAVE</span>
    <span class="quote__drip">KILLED</span>
    <span class="quote__line">MY WIFE</span>
    <span class="quote__line">I’M GLAD SHE’S</span>
    <span class="quote__drip">DEAD</span>
  </div>
  <div class="offer">
    <p class="offer__tour">Harbourside Buried Past Walk</p>
    <p class="offer__discount">25%DISCOUNT</p>
    <p class="offer__label">Offer Codeword</p>
    <p class="offer__code">DARK</p>
  </div>
  <p class="web">www.hollowlantern-tours.com.au</p>
  <svg class="torn-band" viewBox="0 0 462 48" preserveAspectRatio="none" aria-hidden="true">
    <polygon fill="#c8101a" points="0,14 30,10 62,18 95,8 130,15 170,6 210,14 250,9 290,17 330,7 370,13 410,8 440,15 462,10 462,48 0,48"/>
  </svg>
</section>

<section class="flyer flyer--back" aria-label="Flyer back">
  <div class="blood-splatter" role="img" aria-label="Red blood splatter"></div>
  <div class="quote">
    <span class="quote__drip">SHE'S</span>
    <span class="quote__line">A BEAUTIFUL CHILD</span>
    <span class="quote__line">ISN'T SHE?</span>
    <span class="quote__line quote__line--gap">SHE'S THE CAUSE</span>
    <span class="quote__line">OF ALL THE</span>
    <span class="quote__drip">TROUBLE</span>
  </div>
  <svg class="torn-band" viewBox="0 0 461 264" preserveAspectRatio="none" aria-hidden="true">
    <polygon fill="#b10d15" points="0,14 40,8 80,16 120,6 160,12 200,4 240,10 280,3 320,12 360,6 400,14 440,8 461,12 461,246 430,240 390,250 350,238 310,246 270,236 230,248 190,240 150,250 110,238 70,246 30,240 0,248"/>
  </svg>
  <div class="blurb">
    <p>Hollow lantern brings back Newcastle's hidden past, the forgotten past, the dark past that may not want to be remembered.</p>
    <p>Real stories from the streets around you. Discover the histories you won't hear anywhere else. The forgotten stories of yesteryear finally get a chance to be told. Through you they get to live again.</p>
  </div>
  <div class="brand"><span class="brand__mark"></span><span>HOLLOW LANTERN</span></div>
  <p class="booking-note">OUR WEBSITE, BOOKING<br>FORM AND CONTACT DETAILS<br>CAN BE VIEWED AT</p>
  <p class="web">www.hollowlantern-tours.com.au</p>
</section>

</body>
</html>
```